Verdant Banner Design

We need 3 Banners for our superfood supplement e-commerce store.

1. Banner that advertises the food combining chart Dimensions 417 × 464 https://verdantlift.net/content/11-food-combining-rules

2. We need a banner that advertises our subscription program. (Dimensions 388 × 219)

3. We need a banner that highlights our ingredients. (Dimensions 388 × 215)

Our website: https://verdantlift.net/

1. The sizes are in dimensions.

2. Yes the banners are for our website, replacing the ones on the front page now https://verdantlift.net/

Content of Banners

1. Advertisng the food combining chart.

2. Advertising our Subscription program.

3 Advertising our ingredients.

Just use words like:

"Combine the right foods"

Target Market(s)

Organic Superfood Supplement

Contact Information for Business Card

The Business card has to be double sided and must have our logo

Colors

Designer to choose colors to be used in the design.

Requirements
Must have
• 1. You can use the attached images or not, it is up to you, please be creative.
• 2. Please provide the Raw AI files, and also give it in the following formats: JPEG, PNG,
• 3. I have added a file in the brief called subscription image please use to get an idea of the type of banner we are looking for, of course using our product images
Nice to have
• 1. Please show business card design as well, this will help us decide to choose you.
• 2. Please read the ingredients on the product itself, and if you can use some images for the ingredient banner that would be good.
• 3. The business card should have the following:
• Name: Rupert Halvey
• Title: Co-Founder
• Address: Baldwin, NY
• Logo (see attached)
• Phone #: 855-640-3918
• Mobile #: 646-508-2274
• Email: info@verdantlift.net
• Website: www.verdantlift.net
Should not have
• No meat or dairy products in your images

```html
<!DOCTYPE html>
<html lang="en">
<head>
<meta charset="utf-8">
<title>Combine the Right Foods – Verdant</title>
<link rel="stylesheet" href="https://fonts.googleapis.com/css2?family=Lobster&display=swap">
<style>
  :root {
    --board-light: #f3f4f3;
    --board-mid: #e4e7e6;
    --board-seam: #3a3d3a;
    --ink-olive: #2f3222;
    --produce-green: #b9d86a;
    --produce-warm: #d9a070;
  }
  html, body {
    margin: 0;
    padding: 0;
    overflow: hidden;
  }
  .banner {
    position: relative;
    width: 1078px;
    height: 1200px;
    overflow: hidden;
    background: linear-gradient(180deg, var(--board-light) 0%, var(--board-mid) 100%);
  }
  .plank-seams {
    position: absolute;
    inset: 0;
    width: 1078px;
    height: 1200px;
  }
  .plank-seams line {
    stroke: var(--board-seam);
    stroke-width: 2;
    opacity: 0.55;
  }
  .banner-title {
    position: absolute;
    top: 31px;
    left: 0;
    width: 100%;
    margin: 0;
    text-align: center;
    font-family: "Lobster", cursive;
    font-weight: 400;
    font-size: 207px;
    line-height: 176px;
    color: var(--ink-olive);
    letter-spacing: 3px;
  }
  .banner-title .line {
    display: block;
    white-space: nowrap;
  }
  .produce-photo {
    position: absolute;
    left: 0;
    top: 472px;
    width: 1078px;
    height: 648px;
    background: linear-gradient(90deg, var(--produce-green) 0%, var(--produce-warm) 100%);
  }
</style>
</head>
<body>
  <main class="banner">
    <svg class="plank-seams" viewBox="0 0 1078 1200" aria-hidden="true">
      <line x1="146" y1="0" x2="144" y2="1200"/>
      <line x1="318" y1="0" x2="316" y2="1200"/>
      <line x1="488" y1="0" x2="490" y2="1200"/>
      <line x1="660" y1="0" x2="662" y2="1200"/>
      <line x1="786" y1="0" x2="788" y2="1200"/>
      <line x1="940" y1="0" x2="938" y2="1200"/>
    </svg>
    <h1 class="banner-title">
      <span class="line">Combine the</span>
      <span class="line">Right Foods</span>
    </h1>
    <div class="produce-photo" role="img" aria-label="Photo of fresh fruit: green grapes, red plums, an orange, green and red apples and halved limes"></div>
  </main>
</body>
</html>
```